Professional PowerPoint Template for Data Reports, Presentations

We are a small leadership coaching/consulting firm and would like to update our PowerPoint template that we use with our clients, who are typically mid-senior level company professionals. I've attached a sample Powerpoint as well as our branding guide. The cover page is what needs the most work - just doesn't look current/professional enough. We do want to keep the pages after that clean, with come color but enough space for text and graphics.
Target Market(s)
Senior mgmt and HR executives in small-mid sized companies
Font styles to use
Sans Serif
Requirements
Must have
- Professional
- Clean
- Tied to company color scheme/logo
Nice to have
- Our title pages don't usually have many words on them; we'd like a design that has a lot of color - probably still using mainly our blue but accented with other colors.
- Need simple but smart looking pages after cover with lot of space; mostly we have text on the slides. Currently this is often in bullet point style, but we could probably upgrade the options there.
Should not have
- Anything that looks like a marketing style, as we typically use these with our current clients to share results of data collected, project plans, etc.

```html
<!DOCTYPE html>
<html lang="en">
<head>
<meta charset="utf-8">
<title>Brightwell Partners – Slide Template Sheet</title>
<link href="https://fonts.googleapis.com/css2?family=Montserrat:wght@700;800&family=Arimo:wght@400;700&display=swap" rel="stylesheet">
<style>
  :root{
    --navy:#3d4e78;
    --brand-blue:#1f4e82;
    --orange:#e8825a;
    --green:#7fb09b;
    --lavender:#ddd6ea;
    --sand:#f1ede9;
    --ink:#2a2a2a;
    --paper:#ffffff;
    --slide-bg:#fcfcfd;
    --stone:#c9c9c7;
    --sky:#5e8fc4;
  }
  *{box-sizing:border-box;margin:0;padding:0}
  html,body{width:1040px;height:1200px;overflow:hidden;background:var(--paper)}
  body{position:relative;font-family:"Arimo",Arial,sans-serif;color:var(--ink)}
  .sheet{position:absolute;left:40px;top:54px;width:954px;height:1074px;border:1px solid #111}
  .slide{position:absolute;width:477px;height:358px;background:var(--slide-bg);overflow:hidden;border:1px solid #111}
  .slide.edge{border-right:3px solid var(--brand-blue)}
  .c1{left:0}.c2{left:477px}
  .r1{top:0}.r2{top:358px}.r3{top:716px}
  .abs{position:absolute}
  .title{font-family:"Montserrat",Arial,sans-serif;font-weight:800;font-size:15px;letter-spacing:3px;color:var(--navy);line-height:1}
  .title .accent{color:var(--green)}
  .bar{position:absolute;height:3px;display:flex}
  .bar span{flex:1}
  .bar .b1{background:var(--navy)}.bar .b2{background:var(--orange)}.bar .b3{background:var(--green)}
  .bar .b4{background:var(--lavender)}.bar .b5{background:var(--sand)}
  .body{font-size:7.2px;line-height:9.6px;color:var(--ink)}
  .just{text-align:justify}
  .right{text-align:right}
  .center{text-align:center}
  .item-title{font-size:7.6px;font-weight:700;color:var(--navy);text-decoration:underline;margin-bottom:3px}
  .footer{position:absolute;left:0;right:0;bottom:4px;text-align:center;font-size:4.6px;color:#333}
  .tab{position:absolute;right:0;top:23px;width:19px;height:73px;background:var(--brand-blue);display:flex;flex-direction:column;align-items:center;padding-top:6px;gap:5px}
  .tab .dot{width:6px;height:6px;border:1.2px solid #fff;border-radius:50%}
  .tab .name{writing-mode:vertical-rl;transform:rotate(180deg);color:#fff;font-family:"Montserrat",Arial,sans-serif;font-weight:700;font-size:5.6px;letter-spacing:1px}
  .photo-stone{background:linear-gradient(135deg,#d9d9d7,#b9b9b6)}
  .photo-desk{background:linear-gradient(160deg,#e4e1d6 0%,#d6d2c3 55%,#6f6a55 80%,#3f3b33 100%)}
  .photo-chair{background:linear-gradient(180deg,#f2f2f0 0%,#ebebe8 60%,#b8b3a3 80%,#e9e9e6 100%)}
  .photo-sky{background:linear-gradient(160deg,#5f8fc6 0%,#7aa3cf 100%)}
  .checkbox{position:absolute;width:26px;height:26px}
  .checkbox .shadow{position:absolute;left:-3px;top:-3px;width:24px;height:24px}
  .checkbox .box{position:absolute;inset:0;border:2.4px solid var(--navy);background:var(--paper)}
  .icon{position:absolute;width:50px;height:50px}
  .icon .shadow{position:absolute;left:-4px;top:-4px;width:48px;height:48px}
  .icon .box{position:absolute;inset:0;border:2.4px solid var(--navy);background:var(--paper);padding:7px}
  .icon .glyph{width:100%;height:100%;background:linear-gradient(135deg,#e3e6ee,#c9cfdd)}
  .col{position:absolute;width:104px;margin-left:-52px}
</style>
</head>
<body>
<div class="sheet">

  <!-- Slide: two pictures, text right -->
  <section class="slide c1 r1 edge">
    <div class="abs" style="left:42px;top:59px;width:145px;height:150px;background:var(--orange)"></div>
    <div class="abs photo-stone" style="left:37px;top:64px;width:146px;height:146px" role="img" aria-label="Photo of cracked grey concrete texture"></div>
    <div class="abs" style="left:91px;top:124px;width:162px;height:166px;background:var(--lavender)"></div>
    <div class="abs photo-desk" style="left:99px;top:117px;width:162px;height:162px" role="img" aria-label="Photo of a bright home office desk with plants"></div>
    <div class="abs title" style="left:281px;top:122px">TWO PICTURES</div>
    <div class="abs title" style="left:281px;top:146px"><span class="accent">SLIDE</span></div>
    <div class="bar" style="left:281px;top:172px;width:140px"><span class="b5"></span><span class="b4"></span><span class="b3"></span><span class="b2"></span><span class="b1"></span></div>
    <p class="abs body just" style="left:281px;top:194px;width:143px">Lorem ipsum dolor sit amet, ut qui tale interesset, pri eu zril solet altera. Quo graeco detracto indoctum ex, vocent oportere usu no, at cetero corpora forensibus per. Eos suas equidem an, per quando nullam rationibus cu, sit solet dicunt habemus ne. Ius vivendum delicatissimi at, ut nec graeci postulant, nec cu sonet essent.</p>
    <div class="tab"><span class="dot"></span><span class="name">BRIGHTWELL</span></div>
    <p class="footer">© Brightwell Partners www.brightwellpartners.com 555-014-0199</p>
  </section>

  <!-- Slide: two pictures, text left -->
  <section class="slide c2 r1 edge">
    <div class="abs" style="left:231px;top:59px;width:145px;height:150px;background:var(--green)"></div>
    <div class="abs photo-stone" style="left:226px;top:64px;width:146px;height:146px" role="img" aria-label="Photo of cracked grey concrete texture"></div>
    <div class="abs" style="left:279px;top:124px;width:170px;height:166px;background:var(--sand)"></div>
    <div class="abs photo-desk" style="left:287px;top:117px;width:162px;height:162px" role="img" aria-label="Photo of a bright home office desk with plants"></div>
    <div class="abs title right" style="left:40px;top:122px;width:163px">TWO PICTURES</div>
    <div class="abs title right" style="left:40px;top:146px;width:163px"><span class="accent">SLIDE</span></div>
    <div class="bar" style="left:60px;top:172px;width:143px"><span class="b5"></span><span class="b4"></span><span class="b3"></span><span class="b2"></span><span class="b1"></span></div>
    <p class="abs body right" style="left:66px;top:194px;width:139px">Lorem ipsum dolor sit amet, ut qui tale interesset, pri eu zril solet altera. Quo graeco detracto indoctum ex, vocent oportere usu no, at cetero corpora forensibus per. Eos suas equidem an, per quando nullam rationibus cu, sit solet dicunt habemus ne. Ius vivendum delicatissimi at, ut nec graeci postulant, nec cu sonet essent.</p>
    <div class="tab"><span class="dot"></span><span class="name">BRIGHTWELL</span></div>
    <p class="footer">© Brightwell Partners www.brightwellpartners.com 555-014-0199</p>
  </section>

  <!-- Slide: list with photo column -->
  <section class="slide c1 r2">
    <div class="abs photo-chair" style="left:138px;top:0;width:134px;height:358px" role="img" aria-label="Photo of a beige chair at a white desk"></div>
    <div class="abs" style="left:272px;top:0;width:52px;height:358px;background:var(--lavender)"></div>
    <div class="abs title right" style="left:20px;top:75px;width:93px">LIST</div>
    <div class="abs title right" style="left:20px;top:99px;width:93px">SLIDE</div>
    <div class="bar" style="left:32px;top:126px;width:81px"><span class="b1"></span><span class="b2"></span><span class="b3"></span><span class="b4"></span><span class="b5"></span></div>
    <p class="abs body right" style="left:27px;top:141px;width:86px">Lorem ipsum dolor sit amet, ut qui tale interesset, pri eu zril solet altera. Quo graeco detracto indoctum ex, vocent oportere usu no, at cetero corpora forensibus per. Eos suas equidem an, per quando nullam rationibus cu, sit solet dicunt habemus.</p>

    <div class="checkbox" style="left:290px;top:65px"><span class="shadow" style="background:var(--lavender)"></span><span class="box"></span></div>
    <div class="checkbox" style="left:290px;top:126px"><span class="shadow" style="background:var(--orange)"></span><span class="box"></span></div>
    <div class="checkbox" style="left:290px;top:189px"><span class="shadow" style="background:var(--navy)"></span><span class="box"></span></div>
    <div class="checkbox" style="left:290px;top:254px"><span class="shadow" style="background:var(--lavender)"></span><span class="box"></span></div>

    <div class="abs" style="left:329px;top:63px;width:124px"><p class="item-title">First Thing</p><p class="body just">Lorem ipsum dolor sit amet, consectetuer adipiscing elit, sed diam nonummy.</p></div>
    <div class="abs" style="left:329px;top:124px;width:124px"><p class="item-title">Second Thing</p><p class="body just">Lorem ipsum dolor sit amet, consectetuer adipiscing elit, sed diam nonummy.</p></div>
    <div class="abs" style="left:329px;top:187px;width:124px"><p class="item-title">Third Thing</p><p class="body just">Lorem ipsum dolor sit amet, consectetuer adipiscing elit, sed diam nonummy.</p></div>
    <div class="abs" style="left:329px;top:253px;width:124px"><p class="item-title">Fourth Thing</p><p class="body just">Lorem ipsum dolor sit amet, consectetuer adipiscing elit, sed diam nonummy.</p></div>
  </section>

  <!-- Slide: six icon list -->
  <section class="slide c2 r2 edge">
    <div class="abs title center" style="left:0;right:0;top:38px">LIST SLIDE</div>
    <div class="bar" style="left:186px;top:59px;width:107px"><span class="b1"></span><span class="b2"></span><span class="b3"></span><span class="b4"></span><span class="b5"></span></div>

    <div class="icon" style="left:70px;top:82px"><span class="shadow" style="background:var(--green)"></span><div class="box"><div class="glyph" role="img" aria-label="Icon of a target with arrow"></div></div></div>
    <div class="icon" style="left:214px;top:82px"><span class="shadow" style="background:var(--orange)"></span><div class="box"><div class="glyph" role="img" aria-label="Icon of stairs with a flag"></div></div></div>
    <div class="icon" style="left:357px;top:82px"><span class="shadow" style="background:var(--lavender)"></span><div class="box"><div class="glyph" role="img" aria-label="Icon of a team with a check mark"></div></div></div>
    <div class="icon" style="left:67px;top:206px"><span class="shadow" style="background:var(--lavender)"></span><div class="box"><div class="glyph" role="img" aria-label="Icon of a presenter at a chart"></div></div></div>
    <div class="icon" style="left:211px;top:206px"><span class="shadow" style="background:var(--green)"></span><div class="box"><div class="glyph" role="img" aria-label="Icon of a group of people"></div></div></div>
    <div class="icon" style="left:354px;top:206px"><span class="shadow" style="background:var(--orange)"></span><div class="box"><div class="glyph" role="img" aria-label="Icon of a briefcase with a pie chart"></div></div></div>

    <div class="col center" style="left:95px;top:139px"><p class="item-title">First Thing</p><p class="body">Lorem ipsum dolor sit amet, consectetuer adipiscing elit, sed diam nonummy.</p></div>
    <div class="col center" style="left:239px;top:139px"><p class="item-title">Second Thing</p><p class="body">Lorem ipsum dolor sit amet, consectetuer adipiscing elit, sed diam nonummy.</p></div>
    <div class="col center" style="left:382px;top:139px"><p class="item-title">Third Thing</p><p class="body">Lorem ipsum dolor sit amet, consectetuer adipiscing elit, sed diam nonummy.</p></div>
    <div class="col center" style="left:92px;top:263px"><p class="item-title">Fourth Thing</p><p class="body">Lorem ipsum dolor sit amet, consectetuer adipiscing elit, sed diam nonummy.</p></div>
    <div class="col center" style="left:236px;top:263px"><p class="item-title">Fifth Thing</p><p class="body">Lorem ipsum dolor sit amet, consectetuer adipiscing elit, sed diam nonummy.</p></div>
    <div class="col center" style="left:379px;top:263px"><p class="item-title">Sixth Thing</p><p class="body">Lorem ipsum dolor sit amet, consectetuer adipiscing elit, sed diam nonummy.</p></div>

    <div class="tab"><span class="dot"></span><span class="name">BRIGHTWELL</span></div>
    <p class="footer">© Brightwell Partners www.brightwellpartners.com 555-014-0199</p>
  </section>

  <!-- Slide: list with colour block -->
  <section class="slide c1 r3">
    <div class="abs" style="left:284px;top:0;width:9px;height:358px;background:var(--lavender)"></div>
    <div class="abs" style="left:293px;top:0;width:23px;height:358px;background:var(--green)"></div>
    <div class="abs" style="left:316px;top:0;width:161px;height:358px;background:var(--navy)"></div>
    <div class="abs photo-sky" style="left:256px;top:82px;width:179px;height:194px" role="img" aria-label="Photo of a building corner with a loudspeaker against blue sky"></div>
    <div class="abs title right" style="left:60px;top:45px;width:172px">LIST SLIDE</div>
    <div class="bar" style="left:124px;top:69px;width:108px"><span class="b1"></span><span class="b2"></span><span class="b3"></span><span class="b4"></span><span class="b5"></span></div>

    <div class="checkbox" style="left:205px;top:96px"><span class="shadow" style="background:var(--orange);left:3px"></span><span class="box"></span></div>
    <div class="checkbox" style="left:205px;top:151px"><span class="shadow" style="background:var(--navy);left:3px"></span><span class="box"></span></div>
    <div class="checkbox" style="left:205px;top:211px"><span class="shadow" style="background:var(--lavender);left:3px"></span><span class="box"></span></div>
    <div class="checkbox" style="left:205px;top:274px"><span class="shadow" style="background:var(--green);left:3px"></span><span class="box"></span></div>

    <div class="abs right" style="left:82px;top:96px;width:112px"><p class="item-title">First Thing</p><p class="body">Lorem ipsum dolor sit amet, consectetuer adipiscing elit, sed diam nonummy.</p></div>
    <div class="abs right" style="left:82px;top:151px;width:112px"><p class="item-title">Second Thing</p><p class="body">Lorem ipsum dolor sit amet, consectetuer adipiscing elit, sed diam nonummy.</p></div>
    <div class="abs right" style="left:82px;top:211px;width:112px"><p class="item-title">Third Thing</p><p class="body">Lorem ipsum dolor sit amet, consectetuer adipiscing elit, sed diam nonummy.</p></div>
    <div class="abs right" style="left:82px;top:273px;width:112px"><p class="item-title">Fourth Thing</p><p class="body">Lorem ipsum dolor sit amet, consectetuer adipiscing elit, sed diam nonummy.</p></div>
  </section>

  <!-- Slide: four column team list -->
  <section class="slide c2 r3 edge">
    <div class="abs title center" style="left:0;right:0;top:38px">LIST SLIDE</div>
    <p class="abs center" style="left:0;right:0;top:62px;font-size:11px;color:var(--ink)">Lorem ipsum dolor sit amet.</p>
    <div class="bar" style="left:194px;top:85px;width:80px"><span class="b1"></span><span class="b2"></span><span class="b3"></span><span class="b4"></span><span class="b5"></span></div>

    <div class="icon" style="left:59px;top:122px;width:56px;height:56px"><span class="shadow" style="background:var(--green);width:54px;height:54px;left:-6px;top:-6px"></span><div class="box"><div class="glyph" role="img" aria-label="Icon of a team of three people"></div></div></div>
    <div class="icon" style="left:162px;top:122px;width:56px;height:56px"><span class="shadow" style="background:var(--navy);width:54px;height:54px;left:-6px;top:-6px"></span><div class="box"><div class="glyph" role="img" aria-label="Icon of a trophy"></div></div></div>
    <div class="icon" style="left:264px;top:122px;width:56px;height:56px"><span class="shadow" style="background:var(--orange);width:54px;height:54px;left:-6px;top:-6px"></span><div class="box"><div class="glyph" role="img" aria-label="Icon of two people discussing a question"></div></div></div>
    <div class="icon" style="left:359px;top:122px;width:56px;height:56px"><span class="shadow" style="background:var(--lavender);width:54px;height:54px;left:-6px;top:-6px"></span><div class="box"><div class="glyph" role="img" aria-label="Icon of a rising line chart"></div></div></div>

    <div class="col center" style="left:87px;top:189px;width:80px;margin-left:-40px"><p class="item-title">Name Here</p><p class="body" style="margin-top:6px">Lorem ipsum dolor sit amet, consectetuer adipiscing elit, sed diam nonummy nibh euismod tincidunt ut laoreet dolore. Id eam aliquid sadipscing. At per singulis ocurreret. An vim dolore interpretaris.</p></div>
    <div class="col center" style="left:190px;top:189px;width:80px;margin-left:-40px"><p class="item-title">Name Here</p><p class="body" style="margin-top:6px">Lorem ipsum dolor sit amet, consectetuer adipiscing elit, sed diam nonummy nibh euismod tincidunt ut laoreet dolore. Id eam aliquid sadipscing. At per singulis ocurreret. An vim dolore interpretaris.</p></div>
    <div class="col center" style="left:292px;top:189px;width:80px;margin-left:-40px"><p class="item-title">Name Here</p><p class="body" style="margin-top:6px">Lorem ipsum dolor sit amet, consectetuer adipiscing elit, sed diam nonummy nibh euismod tincidunt ut laoreet dolore. Id eam aliquid sadipscing. At per singulis ocurreret. An vim dolore interpretaris.</p></div>
    <div class="col center" style="left:387px;top:189px;width:80px;margin-left:-40px"><p class="item-title">Name Here</p><p class="body" style="margin-top:6px">Lorem ipsum dolor sit amet, consectetuer adipiscing elit, sed diam nonummy nibh euismod tincidunt ut laoreet dolore. Id eam aliquid sadipscing. At per singulis ocurreret. An vim dolore interpretaris.</p></div>

    <div class="tab"><span class="dot"></span><span class="name">BRIGHTWELL</span></div>
    <p class="footer">© Brightwell Partners www.brightwellpartners.com 555-014-0199</p>
  </section>

</div>
</body>
</html>
```